Helicopter scenic /Charter company

Need a sign 920mm x 920mm for our Westbrook Helipad fence that catches the eye for people walking past. Some photos have been attached but feel free to use helicopter photos you have as well. Like the sign to be black with lettering that stands out. You may do a design with photos or it may look better without. It is up to you. It just has to look eye catching and exciting.
Text: Helicopter Joy Flights & Scenic Tours here seven days from October to March. Prices from just $99 per person* Details at skyquilla.com.au or ph 9627 3105
* $99 flights are shared 8 minute flights and are only available on weekends

Target Market(s)

Tourists locals walking past the helipad

Requirements
Must have
• Logo
• Text as in project description

```html
<!DOCTYPE html>
<html lang="en">
<head>
<meta charset="utf-8">
<title>Skyquilla Helicopters – Helipad Sign</title>
<link rel="stylesheet" href="https://fonts.googleapis.com/css2?family=Oswald:wght@500;700&family=Montserrat:wght@500;600;800&family=Roboto:wght@700&display=swap">
<style>
  :root {
    --backdrop: #d4d4d4;
    --black: #121212;
    --yellow: #ffd200;
    --blue: #0f6fb5;
    --blue-deep: #0b5f9e;
    --white: #ffffff;
    --silver: #d9dde2;
    --sea: #2cb5c8;
    --sea-deep: #1a8fb0;
    --sand: #e8dcc2;
    --scrub: #7d8f5a;
  }
  * { margin: 0; padding: 0; box-sizing: border-box; }
  html, body {
    width: 1200px; height: 903px; overflow: hidden;
    background: var(--backdrop);
  }
  .sign {
    position: absolute; left: 170px; top: 21px;
    width: 860px; height: 860px;
    background: var(--black);
    overflow: hidden;
  }
  .sign-header {
    position: absolute; left: 0; top: 0; width: 860px; height: 153px;
    background: var(--black); text-align: center;
  }
  .headline {
    position: absolute; left: 0; right: 0; top: 38px;
    font-family: "Oswald", sans-serif; font-weight: 700;
    font-size: 46px; line-height: 56px; letter-spacing: 0.2px;
    color: var(--yellow); text-transform: uppercase;
  }
  .season {
    position: absolute; left: 0; right: 0; top: 98px;
    font-family: "Montserrat", sans-serif; font-weight: 500;
    font-size: 28px; line-height: 36px; letter-spacing: 1px;
    color: var(--white); text-transform: uppercase;
  }
  .hero-photo {
    position: absolute; left: 0; top: 153px; width: 860px; height: 567px;
    background:
      linear-gradient(125deg, var(--sea-deep) 0%, var(--sea) 35%, #5fc9d4 52%, var(--sand) 62%, #c9c09a 74%, var(--scrub) 88%, #6a7d52 100%);
  }
  .price-badge {
    position: absolute; left: 509px; top: 172px; width: 320px; height: 320px;
  }
  .badge-label { font-family: "Oswald", sans-serif; font-weight: 500; fill: var(--white); }
  .badge-price { font-family: "Oswald", sans-serif; font-weight: 700; fill: var(--yellow); }
  .badge-note { font-family: "Montserrat", sans-serif; font-weight: 600; fill: var(--white); }
  .badge-note .accent { fill: var(--yellow); }
  .sign-footer {
    position: absolute; left: 0; top: 720px; width: 860px; height: 140px;
  }
  .footer-panel { position: absolute; left: 0; top: 0; }
  .brand {
    position: absolute; left: 40px; top: 34px;
    display: flex; align-items: center; gap: 16px;
  }
  .brand-dot {
    width: 46px; height: 46px; border-radius: 50%; background: var(--blue);
  }
  .brand-name {
    font-family: "Montserrat", sans-serif; font-weight: 800;
    font-size: 27px; line-height: 31px; color: var(--white);
    text-transform: uppercase;
  }
  .contact-phone {
    position: absolute; left: 412px; top: 18px;
    display: flex; align-items: center; gap: 14px;
  }
  .phone-number {
    font-family: "Roboto", sans-serif; font-weight: 700;
    font-size: 68px; line-height: 74px; color: var(--white); letter-spacing: 0.5px;
  }
  .contact-web {
    position: absolute; left: 426px; top: 94px;
    font-family: "Montserrat", sans-serif; font-weight: 500;
    font-size: 24px; line-height: 30px; color: var(--white);
  }
  .contact-web .label { color: var(--yellow); }
</style>
</head>
<body>
  <main class="sign">
    <header class="sign-header">
      <h1 class="headline">Helicopter Joy Flights &amp; Scenic Tours</h1>
      <p class="season">Here seven days from October to March</p>
    </header>

    <div class="hero-photo" role="img" aria-label="Photo of a black helicopter flying low over turquoise sea along a sandy beach and coastal suburb"></div>

    <svg class="price-badge" viewBox="0 0 320 320" aria-label="Prices $99 per person">
      <circle cx="160" cy="160" r="155" fill="var(--yellow)"/>
      <circle cx="160" cy="160" r="143" fill="var(--silver)"/>
      <circle cx="160" cy="160" r="132" fill="var(--blue)"/>
      <circle cx="160" cy="160" r="122" fill="none" stroke="var(--white)" stroke-width="1.6" stroke-dasharray="7 5"/>
      <text class="badge-label" x="160" y="80" text-anchor="middle" font-size="22">PRICES</text>
      <text class="badge-price" x="160" y="150" text-anchor="middle" font-size="70">$99</text>
      <text class="badge-label" x="160" y="202" text-anchor="middle" font-size="44">PERPERSON</text>
      <text class="badge-note" x="160" y="226" text-anchor="middle" font-size="11">Shared <tspan class="accent">8 MINUTE</tspan> flights &amp; are</text>
      <text class="badge-note" x="160" y="240" text-anchor="middle" font-size="11">only available on weekends</text>
    </svg>

    <footer class="sign-footer">
      <svg class="footer-panel" width="860" height="140" viewBox="0 0 860 140">
        <rect x="0" y="0" width="860" height="140" fill="var(--black)"/>
        <polygon points="374,0 860,0 860,140 406,140" fill="var(--blue)"/>
        <rect x="0" y="0" width="860" height="3" fill="var(--blue-deep)"/>
      </svg>

      <div class="brand">
        <span class="brand-dot"></span>
        <span class="brand-name">Skyquilla<br>Helicopters</span>
      </div>

      <div class="contact-phone">
        <svg width="44" height="44" viewBox="0 0 24 24" aria-hidden="true">
          <path fill="var(--yellow)" d="M6.6 10.8a15.1 15.1 0 0 0 6.6 6.6l2.2-2.2c.3-.3.7-.4 1-.2 1.1.4 2.3.6 3.6.6.6 0 1 .4 1 1V20c0 .6-.4 1-1 1C10.6 21 3 13.4 3 4c0-.6.4-1 1-1h3.5c.6 0 1 .4 1 1 0 1.3.2 2.5.6 3.6.1.3 0 .7-.2 1z"/>
          <path fill="none" stroke="var(--yellow)" stroke-width="1.6" stroke-linecap="round" d="M14.5 2.8a7 7 0 0 1 6.7 6.7M14.3 6.2a3.6 3.6 0 0 1 3.5 3.5"/>
        </svg>
        <span class="phone-number">9627 3105</span>
      </div>
      <p class="contact-web"><span class="label">DETAILS AT</span> skyquilla.com.au</p>
    </footer>
  </main>
</body>
</html>
```